New business card design for Pinecrest Hollow Optometry Clinic

We need a new business card design using our existing logo (uploaded). Please do not include eyes, eye exam charts or beaches, water, sand. The logo I uploaded shows our colors of green and blue, but we are open to seeing it in black OR white. We would like to see something modern and fresh. It will need to be 2 sided. On the front we will need to be able to put a doctors name, for example-Dr Marta Kellerman and Associates. We will need to be able to change the name to other doctors names when we send for printing. The back of the card should list the following: 3817 Tarrow St, Alder Cove (P)705-555-0148 (E) info@phoc.ca www.phoc.ca. "We are welcoming new patients" and a line for the appointment date and time. I have uploaded the back of a card to give an example

```html
<!DOCTYPE html>
<html lang="en">
<head>
<meta charset="utf-8">
<title>Pinecrest Hollow Optometry Clinic – Business Card</title>
<link href="https://fonts.googleapis.com/css2?family=Montserrat+Alternates:wght@400;500;600;700&display=swap" rel="stylesheet">
<style>
  :root {
    --stage: #262626;
    --card-dark: #3a3a3a;
    --card-white: #ffffff;
    --panel-grey: #e7e7ec;
    --brand-blue: #3553a6;
    --brand-green: #1f9b4e;
    --ink: #2b2b2b;
    --white: #ffffff;
  }
  * { margin: 0; padding: 0; box-sizing: border-box; }
  html, body {
    width: 1200px; height: 1200px; overflow: hidden;
    background: var(--stage);
    font-family: "Montserrat Alternates", sans-serif;
  }
  .card {
    position: absolute; left: 120px;
    width: 960px; height: 548px;
    border-radius: 4px; overflow: hidden;
    box-shadow: 0 18px 40px rgba(0,0,0,.45);
  }

  /* Front */
  .card-front { top: 36px; background: var(--card-dark); }
  .front-brand {
    position: absolute; inset: 0;
    display: flex; align-items: center; justify-content: center; gap: 28px;
  }
  .front-brand .brand-dot {
    width: 56px; height: 56px; border-radius: 50%;
    background: var(--white);
  }
  .front-brand .brand-name {
    color: var(--white); font-weight: 700; font-size: 44px; line-height: 1.15;
  }

  /* Back */
  .card-back { top: 616px; background: var(--card-white); }
  .welcome-band {
    position: absolute; left: 0; top: 0; width: 100%; height: 82px;
    background: var(--card-dark);
    display: flex; align-items: center; justify-content: center;
    color: var(--white); font-weight: 700; font-size: 40px;
  }
  .appointment-panel {
    position: absolute; left: 0; top: 290px; width: 580px; height: 258px;
    background: var(--panel-grey);
  }
  .back-brand {
    position: absolute; left: 48px; top: 118px;
    color: var(--brand-blue); font-weight: 700; font-size: 34px; line-height: 1.15;
  }
  .field {
    position: absolute; display: flex; align-items: flex-end; gap: 12px;
    color: var(--brand-blue); font-size: 26px;
  }
  .field .rule { flex: 1; border-bottom: 2px solid var(--brand-blue); height: 0; margin-bottom: 6px; }
  .field-doctor { left: 48px; top: 232px; width: 500px; font-weight: 600; }
  .field-date { left: 48px; top: 340px; width: 500px; }
  .field-time { left: 48px; top: 440px; width: 500px; }

  .contact-list {
    position: absolute; left: 612px; top: 130px;
    list-style: none; display: flex; flex-direction: column; gap: 22px;
  }
  .contact-item { display: flex; align-items: flex-start; gap: 16px; font-size: 27px; line-height: 1.15; }
  .contact-item svg { flex: none; width: 34px; height: 34px; margin-top: 1px; }
  .contact-address { color: var(--ink); }
  .contact-phone { color: var(--brand-green); font-weight: 700; }
  .contact-email, .contact-web { color: var(--brand-green); }
</style>
</head>
<body>

<section class="card card-front" aria-label="Card front">
  <div class="front-brand">
    <span class="brand-dot"></span>
    <span class="brand-name">Pinecrest Hollow<br>Optometry Clinic</span>
  </div>
</section>

<section class="card card-back" aria-label="Card back">
  <div class="welcome-band">We are Welcoming New Patients</div>
  <div class="appointment-panel"></div>

  <div class="back-brand">Pinecrest Hollow<br>Optometry Clinic</div>

  <div class="field field-doctor"><span>Doctor:</span><span class="rule"></span></div>
  <div class="field field-date"><span>Date:</span><span class="rule"></span></div>
  <div class="field field-time"><span>Time:</span><span class="rule"></span></div>

  <ul class="contact-list">
    <li class="contact-item contact-address">
      <svg viewBox="0 0 34 34" aria-hidden="true"><circle cx="17" cy="17" r="15.5" fill="none" stroke="#2b2b2b" stroke-width="1.6"/><path d="M17 8a6 6 0 0 0-6 6c0 4.5 6 11 6 11s6-6.5 6-11a6 6 0 0 0-6-6z" fill="none" stroke="#2b2b2b" stroke-width="1.8"/><circle cx="17" cy="14" r="2.2" fill="#2b2b2b"/></svg>
      <span>3817 Tarrow St,<br>Alder Cove</span>
    </li>
    <li class="contact-item contact-phone">
      <svg viewBox="0 0 34 34" aria-hidden="true"><circle cx="17" cy="17" r="15.5" fill="none" stroke="#2b2b2b" stroke-width="1.6"/><path d="M12 9l3 1 1 4-2 1.5a10 10 0 0 0 4.5 4.5L20 18l4 1 1 3-2 2c-6 0-13-7-13-13z" fill="#2b2b2b"/></svg>
      <span>705-555-0148</span>
    </li>
    <li class="contact-item contact-email">
      <svg viewBox="0 0 34 34" aria-hidden="true"><circle cx="17" cy="17" r="15.5" fill="#2b2b2b"/><rect x="9" y="11.5" width="16" height="11" fill="#fff"/><path d="M9 11.5l8 6.5 8-6.5" fill="none" stroke="#2b2b2b" stroke-width="1.6"/></svg>
      <span>info@phoc.ca</span>
    </li>
    <li class="contact-item contact-web">
      <svg viewBox="0 0 34 34" aria-hidden="true"><circle cx="17" cy="17" r="15.5" fill="none" stroke="#2b2b2b" stroke-width="1.6"/><circle cx="17" cy="17" r="9" fill="none" stroke="#2b2b2b" stroke-width="1.5"/><ellipse cx="17" cy="17" rx="4" ry="9" fill="none" stroke="#2b2b2b" stroke-width="1.3"/><path d="M8 17h18M9.5 12.5h15M9.5 21.5h15" stroke="#2b2b2b" stroke-width="1.2"/></svg>
      <span>www.phoc.ca</span>
    </li>
  </ul>
</section>

</body>
</html>
```